Label for Dog Nourishing CBD Balm

Dear Designers,

We are looking for a packaging expert to design our new Hydrating Balm for dogs which contain a relaxing hemp extract (CBD). The product is intended to be massaged on the dog’s paws to make them softer and promote the animal’s well-being :)

Our company is already selling various relaxing cat & dog products, and we would like this new design to reflect the same "style & feeling" as our current products (see attached ZIP file).

Technical aspects:
- The packaging is a 40ml aluminium jar (58mm x 23mm).
- We are looking to design 2 separate labels (one for the front, one for the back)
- The label dimensions should be : 50mm x 50mm
- Please follow technical guidelines from printer (see ZIP file).

Design aspects:
- The design should be compatible with our brand identity (i.e. fluffly, pure, relaxing, positive, clean & natural).
- People should understand what the product "is" and what the product "does" simply from looking at the design.
- The actual balm is white/yellow in color.
- Soft/rounded shapes are preferred.
- Please use our brand's colors (see typo & colors in ZIP file)
- Please use our brand's fonts (see typo & colors in ZIP file)
- Please use our company logo (see ZIP file).
- The design also needs to convey a strong sense of professionalism as we are an animal "healthcare" brand.
- If you want to include a dog picture, we would prefer you to use a picture of our official brand ambassador (see ZIP file).
- Only original work (no plagiarism will be accepted).

Please don't hesitate to send us a message if you have any questions about the brand, the product or the design requirements.

We look forward to seeing your designs & working on this together !

Thanks & regards,
Marcus

Target Market(s)

Dog owners

Font styles to use
Other font styles liked:
• See ZIP file

Requirements
Must have
• Brand fonts (see typo & colors in ZIP file)
Brand colors (see typo & colors in ZIP file)

```html
<!DOCTYPE html>
<html lang="en">
<head>
<meta charset="UTF-8">
<title>Verdalia Soothing Balm Label</title>
<link rel="stylesheet" href="https://fonts.googleapis.com/css2?family=Poppins:wght@500;700;800&display=swap">
<style>
  :root {
    --page-bg: #e4e0dd;
    --label-bg: #e9e8ea;
    --brand-green: #37a787;
    --paw-tint: #b3dcd1;
    --ink: #1b1b1b;
    --brand-dark: #12301f;
    --ring-text: #f4f6f5;
  }
  html, body {
    margin: 0;
    padding: 0;
    width: 1200px;
    height: 1192px;
    overflow: hidden;
    background: var(--page-bg);
  }
  .label {
    display: block;
    width: 1200px;
    height: 1192px;
    font-family: "Poppins", sans-serif;
  }
  .label-face { fill: var(--label-bg); }
  .label-ring { fill: none; stroke: var(--brand-green); stroke-width: 62; }
  .ring-text { fill: var(--ring-text); font-weight: 500; font-size: 44px; letter-spacing: 1px; }
  .net-weight { fill: var(--ring-text); font-weight: 700; font-size: 34px; }
  .brand-name { fill: var(--brand-dark); font-weight: 500; font-size: 66px; letter-spacing: 2px; }
  .brand-sub { fill: var(--brand-green); font-weight: 500; font-size: 24px; }
  .product-name { fill: var(--brand-green); font-weight: 800; font-size: 148px; letter-spacing: 4px; }
  .paw-mark { fill: var(--paw-tint); }
  .strength { fill: var(--ink); font-weight: 800; font-size: 76px; }
  .thc { fill: var(--ink); font-weight: 700; font-size: 46px; }
</style>
</head>
<body>
<svg class="label" viewBox="0 0 1200 1192" xmlns="http://www.w3.org/2000/svg">
  <defs>
    <path id="top-arc" d="M 136,596 A 464 464 0 0 1 1064,596"/>
    <path id="bottom-arc" d="M 108,596 A 492 492 0 0 0 1092,596"/>
  </defs>

  <circle class="label-face" cx="600" cy="596" r="530"/>
  <circle class="label-ring" cx="600" cy="596" r="478"/>

  <text class="ring-text" text-anchor="middle">
    <textPath href="#top-arc" startOffset="50%">REPAIR | NOURISH | PROTECT</textPath>
  </text>
  <text class="net-weight" text-anchor="middle">
    <textPath href="#bottom-arc" startOffset="50%">Net Wt : 40g</textPath>
  </text>

  <g class="brand">
    <text class="brand-name" x="600" y="330" text-anchor="middle">VERDALIA</text>
    <text class="brand-sub" x="690" y="372" text-anchor="middle">For Animals</text>
  </g>

  <g class="paw-mark" role="img" aria-label="Soft paw print graphic">
    <ellipse cx="520" cy="745" rx="34" ry="46"/>
    <ellipse cx="585" cy="715" rx="36" ry="50"/>
    <ellipse cx="655" cy="720" rx="36" ry="50"/>
    <ellipse cx="715" cy="760" rx="32" ry="44"/>
    <path d="M 520,880 C 520,810 570,780 615,780 C 665,780 720,815 720,880 C 720,935 680,945 650,930 C 630,920 600,920 580,930 C 550,945 520,935 520,880 Z"/>
  </g>

  <text class="product-name" x="600" y="590" text-anchor="middle">SOOTHING</text>
  <text class="product-name" x="600" y="730" text-anchor="middle">BALM</text>

  <text class="strength" x="600" y="830" text-anchor="middle">CBD 250mg</text>
  <text class="thc" x="600" y="895" text-anchor="middle">0% THC</text>
</svg>
</body>
</html>
```